The Honeycrisp Are Ready: Announcing Apple Picking At Wren & Tolley

I would like to develop an e-mail notification to send to our subscribers notifying them:
(Announcing to our fans that Honeycrisp Apples are ready for picking)

Header: The Honeycrisp Are Ready!
Now Picking Our Family Favorite Variety
We Wanted To Make Sure You Were The First To Know

Cedar Row Is Open 7 Days A Week For Apple Picking

These Will Not Last Long!

Fall Is Back At Wren & Tolley. This Means Cool, Crisp Fall Days In The Orchard. Warm Cider Donuts & Apple Fritters, Hard Cider Sampling, Pony Rides, Apple Picking & Much More. Come Join Us And Make Fall Memories That Will Last For Generations To Come.

Target Market(s)

Families Looking For Activities In The Fall

Industry/Entity Type

Agri-Tourism

Font styles to use
Other font styles liked:
• DDC Hardware

Colors
0054AA
0677BA
7BADD7
CADEEF
E8F1F8
EB3D1F
EC4F4E
F09395
F8D3D4
FCEDEE

Requirements
Must have
• Call To Action: The Honeycrisp Are Ready!
Nice to have
• Images of the orchard and people picking apples. Please take a look at our website: www.wrenandtolleyorchard.com for inspiration

```html
<!DOCTYPE html>
<html lang="en">
<head>
<meta charset="utf-8">
<title>The Honeycrisp Are Ready! – Wren &amp; Tolley</title>
<link rel="stylesheet" href="https://fonts.googleapis.com/css2?family=Bebas+Neue&family=Oswald:wght@400;500&family=Kaushan+Script&display=swap">
<style>
  :root {
    --ink: #111111;
    --apple-red: #c8202f;
    --paper: #f4f4f4;
    --scene-light: #ededed;
    --scene-mid: #c9c9c9;
    --scene-dark: #9a9a9a;
    --placeholder-warm: #c98a6a;
    --placeholder-red: #c4545a;
    --placeholder-grey: #8a8a8a;
    --photo-frame: #ffffff;
  }
  * { box-sizing: border-box; margin: 0; padding: 0; }
  html, body { width: 1200px; height: 866px; overflow: hidden; background: var(--paper); }
  .announcement {
    position: relative;
    width: 1200px;
    height: 866px;
    overflow: hidden;
    font-family: "Oswald", sans-serif;
    color: var(--ink);
  }
  .orchard-backdrop {
    position: absolute; inset: 0;
    background:
      linear-gradient(180deg, rgba(255,255,255,0.85) 0%, rgba(255,255,255,0.55) 35%, rgba(255,255,255,0.45) 70%, rgba(255,255,255,0.7) 100%),
      linear-gradient(180deg, var(--scene-light) 0%, var(--scene-mid) 45%, var(--scene-dark) 75%, var(--scene-mid) 100%);
  }
  .abs { position: absolute; white-space: nowrap; }

  .headline {
    left: 321px; top: 72px; width: 470px;
    font-family: "Bebas Neue", sans-serif;
    font-size: 104px; line-height: 1;
    text-align: center;
    letter-spacing: 1px;
    transform: scaleX(0.86);
    transform-origin: left top;
  }
  .headline-script {
    left: 462px; top: 176px;
    font-family: "Kaushan Script", cursive;
    font-size: 72px; line-height: 1.1;
    color: var(--apple-red);
  }
  .rule { position: absolute; }

  .orchard-photo {
    left: 848px; top: 72px; width: 298px; height: 222px;
    background: var(--photo-frame);
    padding: 10px;
    transform: rotate(8deg);
    box-shadow: 0 3px 10px rgba(0,0,0,0.35);
  }
  .orchard-photo .photo-fill {
    width: 100%; height: 100%;
    background: radial-gradient(circle at 55% 45%, #7a9a48 0%, #3f6a2a 55%, #2b4a1e 100%);
  }

  .placeholder { border-radius: 6px; }
  .basket-art {
    left: 80px; top: 248px; width: 310px; height: 190px;
    background: linear-gradient(180deg, var(--placeholder-red) 0%, var(--placeholder-warm) 100%);
  }
  .apple-art {
    left: 396px; top: 302px; width: 82px; height: 114px;
    background: linear-gradient(180deg, var(--placeholder-red) 0%, var(--apple-red) 100%);
  }
  .small-apple-art {
    left: 846px; top: 788px; width: 40px; height: 40px;
    background: var(--placeholder-red);
  }
  .truck-art {
    left: 890px; top: 686px; width: 247px; height: 124px;
    background: linear-gradient(180deg, var(--placeholder-grey) 0%, #4a4a4a 100%);
  }

  .subline {
    font-family: "Oswald", sans-serif;
    font-weight: 500;
    font-size: 42px; line-height: 1;
    transform: scaleX(0.75);
    transform-origin: right top;
    text-align: right;
  }
  .subline--one { right: 349px; top: 312px; }
  .subline--two { right: 349px; top: 368px; }
  .subline--three { left: 311px; top: 456px; transform: scaleX(0.79); transform-origin: left top; text-align: left; }

  .first-to-know {
    left: 482px; top: 518px;
    font-family: "Oswald", sans-serif;
    font-weight: 500;
    font-size: 68px; line-height: 1;
    color: var(--apple-red);
    transform: scaleX(0.72);
    transform-origin: left top;
  }

  .hours {
    left: 249px; top: 646px;
    font-family: "Oswald", sans-serif;
    font-weight: 500;
    font-size: 31px; line-height: 1;
    letter-spacing: 3.2px;
    transform: scaleX(0.845);
    transform-origin: left top;
  }

  .closing {
    left: 376px; top: 756px;
    font-family: "Kaushan Script", cursive;
    font-size: 46px; line-height: 1.2;
  }
</style>
</head>
<body>
<main class="announcement">
  <div class="orchard-backdrop" role="img" aria-label="Faded black and white photograph of the Wren &amp; Tolley orchard grounds with barns, picnic tables, a welcome sign and an old flatbed truck"></div>

  <div class="abs orchard-photo">
    <div class="photo-fill" role="img" aria-label="Photograph of ripe red Honeycrisp apples hanging on a leafy tree branch"></div>
  </div>

  <h1 class="abs headline">THE HONEYCRISP</h1>
  <p class="abs headline-script" role="img" aria-label="Are Ready! in red hand lettering">Are Ready!</p>
  <svg class="rule" style="left:494px;top:264px" width="216" height="12" viewBox="0 0 216 12" aria-hidden="true">
    <path d="M2 8 Q108 1 214 5" stroke="var(--ink)" stroke-width="3" fill="none" stroke-linecap="round"/>
  </svg>

  <div class="abs placeholder basket-art" role="img" aria-label="Illustration of a wooden bushel basket full of red apples with leaves"></div>
  <div class="abs placeholder apple-art" role="img" aria-label="Illustration of a single red apple with a green leaf"></div>

  <p class="abs subline subline--one">NOW PICKING OUR FAMILY</p>
  <p class="abs subline subline--two">FAVORITE VARIETY</p>
  <p class="abs subline subline--three">&rsaquo; WE WANTED TO MAKE SURE YOU WERE THE</p>

  <p class="abs first-to-know">FIRST TO KNOW</p>
  <svg class="rule" style="left:520px;top:610px" width="226" height="12" viewBox="0 0 226 12" aria-hidden="true">
    <path d="M2 8 Q113 1 224 6" stroke="var(--ink)" stroke-width="3.5" fill="none" stroke-linecap="round"/>
  </svg>

  <p class="abs hours">CEDAR ROW IS OPEN 7 DAYS A WEEK FOR APPLE PICKING</p>
  <svg class="rule" style="left:608px;top:706px" width="42" height="12" viewBox="0 0 42 12" aria-hidden="true">
    <circle cx="6" cy="6" r="4" fill="var(--ink)"/>
    <circle cx="21" cy="6" r="4" fill="var(--ink)"/>
    <circle cx="36" cy="6" r="4" fill="var(--ink)"/>
  </svg>

  <p class="abs closing" role="img" aria-label="These Will Not Last Long! in black hand lettering">These Will Not Last Long!</p>
  <div class="abs placeholder small-apple-art" role="img" aria-label="Small illustration of a red apple"></div>
  <div class="abs placeholder truck-art" role="img" aria-label="Black and white illustration of a vintage pickup truck carrying red apples"></div>
</main>
</body>
</html>
```